Powerpoint Presentation Template

Kindly design a business class Powepoint Presentation template for our business use. Please stick to our company colours or even pictures as shown on our website and Logo

```html
<!DOCTYPE html>
<html lang="en">
<head>
<meta charset="utf-8">
<title>Kestrel Properties – Presentation Template</title>
<link href="https://fonts.googleapis.com/css2?family=Montserrat:wght@400;600;700;800&display=swap" rel="stylesheet">
<style>
:root{
  --navy:#2d3a4e;
  --navy-2:#34435a;
  --red:#8f2b22;
  --red-dk:#6f1f18;
  --ink:#333a44;
  --grey:#8a8f96;
  --line:#d9dbde;
  --paper:#ffffff;
  --charcoal:#3a3d42;
}
*{margin:0;padding:0;box-sizing:border-box}
html,body{width:1200px;height:1200px;overflow:hidden;background:var(--navy);font-family:"Montserrat",sans-serif}
.board{position:relative;width:1200px;height:1200px}
.brand{position:absolute;left:198px;top:22px;color:var(--red);font-weight:800;font-size:42px;letter-spacing:1px;line-height:1}
.brand-sub{position:absolute;left:226px;top:66px;color:var(--grey);font-weight:400;font-size:26px;line-height:1}
.showcase{position:absolute;left:50px;top:108px;width:490px;height:277px;background:var(--navy-2)}
.sl{position:absolute;width:132px;height:73px;background:var(--paper);overflow:hidden}
.sl.big{width:150px;height:82px}
.sl::after{content:"";position:absolute;left:0;right:0;bottom:0;height:3px;background:var(--red)}
.sl.dark{background:var(--charcoal)}
.sl.maroon{background:var(--red)}
.t{position:absolute;left:5px;top:4px;font-size:3.6px;font-weight:700;color:var(--red);text-transform:uppercase;letter-spacing:.2px}
.dark .t,.maroon .t{color:#fff}
.m{position:absolute;right:4px;top:3px;font-size:4.6px;font-weight:800;color:var(--red)}
.dark .m,.maroon .m{color:#fff}
.ph{position:absolute;background:linear-gradient(160deg,#b3b0a6,#6f6a5f)}
.ph.sky{background:linear-gradient(180deg,#9fb0bd,#7b7466)}
.ph.dim{background:linear-gradient(160deg,#5d6168,#2f3237)}
.p{position:absolute;font-size:2.6px;line-height:3.4px;color:var(--grey)}
.dark .p,.maroon .p{color:#e7d9d7}
.blk{position:absolute;background:var(--red)}
.hero{position:absolute;font-weight:800;color:#fff;text-transform:uppercase;letter-spacing:.3px}
.word{position:absolute;font-weight:800;color:var(--red)}
.chart{position:absolute}
</style>
</head>
<body>
<div class="board">
  <div class="brand">KESTREL</div>
  <div class="brand-sub">Properties</div>

  <!-- featured slides -->
  <div class="showcase">
    <div class="sl big" style="left:10px;top:10px"><span class="t">About us</span><span class="m">KESTREL</span>
      <span class="word" style="left:8px;top:14px;font-size:8px">JOURNEY</span>
      <svg class="chart" style="left:8px;top:30px" width="134" height="40"><polyline points="0,30 25,26 50,22 75,16 100,10 126,4" fill="none" stroke="#8f2b22" stroke-width="1.2" stroke-dasharray="3 2"/><g fill="#8f2b22"><circle cx="25" cy="26" r="2"/><circle cx="50" cy="22" r="2"/><circle cx="75" cy="16" r="2"/><circle cx="100" cy="10" r="2"/></g></svg></div>
    <div class="sl big" style="left:170px;top:10px"><span class="word" style="left:10px;top:18px;font-size:13px">KESTREL</span><span class="p" style="left:10px;top:34px;font-size:5px;color:#666">Properties</span><span class="t" style="top:58px;left:10px">Presentation title</span><div class="ph" style="left:100px;top:0;width:50px;height:79px" role="img" aria-label="Photo of residential buildings"></div></div>
    <div class="sl big maroon" style="left:330px;top:10px"><span class="t">Our history</span><span class="p" style="left:6px;top:14px;width:80px">Add your company history text here in a short line of copy.</span><div class="ph" style="left:90px;top:0;width:60px;height:79px" role="img" aria-label="Photo of a completed housing project"></div></div>
    <div class="sl big" style="left:10px;top:97px"><span class="t">Awards</span><span class="m">KESTREL</span>
      <svg class="chart" style="left:10px;top:22px" width="130" height="40"><g fill="#c9c9c9"><rect x="0" y="6" width="18" height="18"/><circle cx="40" cy="15" r="9"/><rect x="60" y="6" width="18" height="18"/><circle cx="100" cy="15" r="9"/></g></svg></div>
    <div class="sl big dark" style="left:170px;top:97px"><div class="ph dim" style="left:0;top:0;width:150px;height:50px" role="img" aria-label="Photo of a civil construction site"></div><span class="hero" style="left:82px;top:30px;font-size:7px">Civil</span><span class="m" style="top:56px;left:6px;right:auto">KESTREL</span></div>
    <div class="sl big" style="left:330px;top:97px"><span class="t">Our expertise</span><span class="m">KESTREL</span><div class="blk" style="left:6px;top:14px;width:36px;height:62px"></div><div class="ph" style="left:50px;top:40px;width:45px;height:30px" role="img" aria-label="Photo of road works"></div><div class="ph sky" style="left:98px;top:40px;width:45px;height:30px" role="img" aria-label="Photo of earthworks machinery"></div></div>
    <div class="sl big" style="left:10px;top:184px"><span class="t">Your slide title here</span><span class="m">KESTREL</span>
      <svg class="chart" style="left:6px;top:16px" width="140" height="60"><polygon points="0,60 60,60 0,5" fill="#8f2b22"/><g fill="#3a3d42"><rect x="62" y="10" width="12" height="8"/><rect x="62" y="26" width="12" height="8"/><rect x="62" y="42" width="12" height="8"/></g></svg></div>
    <div class="sl big" style="left:170px;top:184px"><span class="t">Your slide title here</span><span class="m">KESTREL</span>
      <svg class="chart" style="left:10px;top:22px" width="130" height="50"><g fill="none" stroke="#8f2b22" stroke-width="2"><circle cx="16" cy="18" r="11"/><circle cx="48" cy="18" r="11"/><circle cx="80" cy="18" r="11"/><circle cx="112" cy="18" r="11"/></g></svg></div>
    <div class="sl big" style="left:330px;top:184px"><span class="t">Property development projects</span><span class="m">KESTREL</span><div class="ph" style="left:6px;top:18px;width:44px;height:26px" role="img" aria-label="Photo of townhouses"></div><div class="ph sky" style="left:53px;top:18px;width:44px;height:26px" role="img" aria-label="Photo of a residential street"></div><div class="ph" style="left:100px;top:18px;width:44px;height:26px" role="img" aria-label="Photo of a housing complex"></div><span class="p" style="left:6px;top:50px">Add your project text here</span></div>
  </div>

  <!-- left column set -->
  <div class="sl dark" style="left:73px;top:410px"><div class="ph dim" style="left:0;top:0;width:132px;height:40px" role="img" aria-label="Photo of a building exterior"></div><span class="hero" style="left:0;right:0;top:10px;text-align:center;font-size:4.5px">Presentation title</span><span class="word" style="left:50px;top:52px;font-size:6px;color:#fff">KESTREL</span></div>
  <div class="sl" style="left:228px;top:410px"><span class="word" style="left:8px;top:12px;font-size:11px">KESTREL</span><span class="p" style="left:8px;top:26px;font-size:5px;color:#555">Properties</span><span class="t" style="left:8px;top:54px">Presentation title</span><div class="ph" style="left:90px;top:0;width:42px;height:70px" role="img" aria-label="Photo of residential buildings"></div></div>
  <div class="sl dark" style="left:382px;top:410px"><div class="ph dim" style="left:0;top:0;width:132px;height:40px" role="img" aria-label="Photo of a building exterior"></div><span class="hero" style="left:0;right:0;top:16px;text-align:center;font-size:4.5px">Presentation title</span><span class="word" style="left:50px;top:52px;font-size:6px;color:#fff">KESTREL</span></div>

  <div class="sl" style="left:73px;top:495px"><span class="word" style="left:34px;top:26px;font-size:12px">KESTREL</span><span class="p" style="left:46px;top:42px;font-size:5px;color:#555">Properties</span></div>
  <div class="sl" style="left:228px;top:495px"><span class="t" style="top:18px">Table of contents</span><span class="word" style="left:8px;top:38px;font-size:6px">KESTREL</span><div class="blk" style="left:70px;top:0;width:62px;height:73px"></div><span class="p" style="left:76px;top:10px;color:#fff">Title goes here<br><br>Title goes here<br><br>Title goes here<br><br>Title goes here</span></div>
  <div class="sl" style="left:382px;top:495px"><div class="blk" style="left:0;top:0;width:58px;height:73px"></div><span class="t" style="color:#fff">Our history</span><span class="p" style="left:5px;top:12px;width:48px;color:#fff">Add a short history of the company here</span><div class="ph" style="left:62px;top:2px;width:68px;height:36px" role="img" aria-label="Photo of a housing estate"></div><span class="p" style="left:62px;top:44px;width:66px">Add your text here</span></div>

  <div class="sl" style="left:73px;top:582px"><span class="t">About us</span><span class="m">KESTREL</span><span class="p" style="left:12px;top:16px">Our vision</span><span class="p" style="left:52px;top:16px">Our mission</span><span class="p" style="left:92px;top:16px">Our values</span><div class="ph" style="left:8px;top:40px;width:80px;height:26px" role="img" aria-label="Photo of a building under construction"></div></div>
  <div class="sl" style="left:228px;top:582px"><span class="t">About us</span><span class="m">KESTREL</span><span class="word" style="left:8px;top:14px;font-size:7px">JOURNEY</span><svg class="chart" style="left:8px;top:26px" width="118" height="40"><polyline points="0,28 24,24 48,20 72,14 96,8 114,2" fill="none" stroke="#8f2b22" stroke-width="1" stroke-dasharray="3 2"/><g fill="#8f2b22"><circle cx="24" cy="24" r="1.8"/><circle cx="48" cy="20" r="1.8"/><circle cx="72" cy="14" r="1.8"/><circle cx="96" cy="8" r="1.8"/></g></svg></div>
  <div class="sl" style="left:382px;top:582px"><div class="ph sky" style="left:0;top:0;width:132px;height:38px" role="img" aria-label="Photo of modern apartment blocks"></div><div class="blk" style="left:0;top:38px;width:132px;height:35px"></div><span class="hero" style="left:6px;top:48px;font-size:5px">Building</span><span class="p" style="left:56px;top:44px;width:70px">Add your text here</span><span class="word" style="left:6px;top:6px;font-size:6px;color:#fff">KESTREL</span></div>

  <div class="sl" style="left:73px;top:674px"><div class="ph dim" style="left:0;top:0;width:132px;height:38px" role="img" aria-label="Photo of a civil construction site"></div><span class="hero" style="left:92px;top:16px;font-size:5px">Civil</span><span class="word" style="left:6px;top:46px;font-size:6px">KESTREL</span><span class="p" style="left:54px;top:44px;width:72px">Add your text here</span></div>
  <div class="sl" style="left:228px;top:674px"><span class="t">Our expertise</span><span class="m">KESTREL</span><div class="blk" style="left:5px;top:12px;width:34px;height:56px"></div><span class="p" style="left:44px;top:14px;width:82px">Add your text here</span><div class="ph" style="left:44px;top:38px;width:40px;height:26px" role="img" aria-label="Photo of road works"></div><div class="ph sky" style="left:87px;top:38px;width:40px;height:26px" role="img" aria-label="Photo of earthworks"></div></div>
  <div class="sl" style="left:382px;top:674px"><span class="t">Our expertise</span><span class="m">KESTREL</span><div class="blk" style="left:5px;top:12px;width:34px;height:56px"></div><span class="p" style="left:44px;top:14px;width:82px">Add your text here</span><div class="ph" style="left:44px;top:38px;width:40px;height:26px" role="img" aria-label="Photo of pipe works"></div><div class="ph sky" style="left:87px;top:38px;width:40px;height:26px" role="img" aria-label="Photo of a water channel"></div></div>

  <div class="sl" style="left:73px;top:758px"><span class="t">Our expertise</span><span class="m">KESTREL</span><div class="blk" style="left:5px;top:12px;width:34px;height:56px"></div><span class="p" style="left:44px;top:14px;width:82px">Add your text here</span><div class="ph" style="left:44px;top:40px;width:38px;height:24px" role="img" aria-label="Photo of a site"></div><div class="ph sky" style="left:85px;top:40px;width:38px;height:24px" role="img" aria-label="Photo of a structure"></div></div>
  <div class="sl" style="left:228px;top:758px"><span class="t">Civil structures</span><span class="m">KESTREL</span><div class="ph" style="left:6px;top:20px;width:28px;height:20px" role="img" aria-label="Construction photo"></div><div class="ph sky" style="left:37px;top:20px;width:28px;height:20px" role="img" aria-label="Construction photo"></div><div class="ph" style="left:68px;top:20px;width:28px;height:20px" role="img" aria-label="Construction photo"></div><div class="ph sky" style="left:99px;top:20px;width:28px;height:20px" role="img" aria-label="Construction photo"></div><div class="ph sky" style="left:6px;top:44px;width:28px;height:20px" role="img" aria-label="Construction photo"></div><div class="ph" style="left:37px;top:44px;width:28px;height:20px" role="img" aria-label="Construction photo"></div><div class="ph sky" style="left:68px;top:44px;width:28px;height:20px" role="img" aria-label="Construction photo"></div><div class="ph" style="left:99px;top:44px;width:28px;height:20px" role="img" aria-label="Construction photo"></div></div>
  <div class="sl dark" style="left:382px;top:758px"><div class="ph" style="left:0;top:0;width:56px;height:70px" role="img" aria-label="Photo of a townhouse"></div><span class="hero" style="left:80px;top:16px;font-size:5px">Property</span><span class="word" style="left:6px;top:50px;font-size:6px;color:#fff">KESTREL</span><span class="p" style="left:60px;top:42px;width:68px">Add your text here</span></div>

  <div class="sl" style="left:73px;top:846px"><span class="t">Our expertise</span><span class="m">KESTREL</span><span class="p" style="left:5px;top:12px;width:122px">Add a short paragraph of text here</span><div class="ph" style="left:6px;top:30px;width:28px;height:30px" role="img" aria-label="Project photo"></div><div class="ph sky" style="left:37px;top:30px;width:28px;height:30px" role="img" aria-label="Project photo"></div><div class="ph" style="left:68px;top:30px;width:28px;height:30px" role="img" aria-label="Project photo"></div><div class="ph sky" style="left:99px;top:30px;width:28px;height:30px" role="img" aria-label="Project photo"></div></div>
  <div class="sl" style="left:228px;top:846px"><span class="t">Property development projects</span><span class="m">KESTREL</span><span class="p" style="left:40px;top:14px">Add project name here</span><div class="ph" style="left:6px;top:22px;width:38px;height:20px" role="img" aria-label="Housing photo"></div><div class="ph sky" style="left:47px;top:22px;width:38px;height:20px" role="img" aria-label="Housing photo"></div><div class="ph" style="left:88px;top:22px;width:38px;height:20px" role="img" aria-label="Housing photo"></div><div class="ph sky" style="left:6px;top:45px;width:38px;height:20px" role="img" aria-label="Housing photo"></div><div class="ph" style="left:47px;top:45px;width:38px;height:20px" role="img" aria-label="Housing photo"></div><div class="ph sky" style="left:88px;top:45px;width:38px;height:20px" role="img" aria-label="Housing photo"></div></div>
  <div class="sl" style="left:382px;top:846px"><span class="t">Property development projects</span><span class="m">KESTREL</span><span class="p" style="left:40px;top:14px">Add project name here</span><div class="ph sky" style="left:6px;top:22px;width:38px;height:20px" role="img" aria-label="Housing photo"></div><div class="ph" style="left:47px;top:22px;width:38px;height:20px" role="img" aria-label="Housing photo"></div><div class="ph sky" style="left:88px;top:22px;width:38px;height:20px" role="img" aria-label="Housing photo"></div><div class="ph" style="left:6px;top:45px;width:38px;height:20px" role="img" aria-label="Housing photo"></div><div class="ph sky" style="left:47px;top:45px;width:38px;height:20px" role="img" aria-label="Housing photo"></div><div class="ph" style="left:88px;top:45px;width:38px;height:20px" role="img" aria-label="Housing photo"></div></div>

  <div class="sl" style="left:73px;top:940px"><span class="t">Property development projects</span><span class="m">KESTREL</span><span class="p" style="left:40px;top:14px">Add project name here</span><div class="ph" style="left:6px;top:24px;width:38px;height:20px" role="img" aria-label="Housing photo"></div><div class="ph sky" style="left:47px;top:24px;width:38px;height:20px" role="img" aria-label="Housing photo"></div><div class="ph" style="left:88px;top:24px;width:38px;height:20px" role="img" aria-label="Housing photo"></div><div class="ph sky" style="left:6px;top:47px;width:38px;height:18px" role="img" aria-label="Housing photo"></div><div class="ph" style="left:47px;top:47px;width:38px;height:18px" role="img" aria-label="Housing photo"></div><div class="ph sky" style="left:88px;top:47px;width:38px;height:18px" role="img" aria-label="Housing photo"></div></div>
  <div class="sl" style="left:228px;top:940px"><div class="ph" style="left:0;top:0;width:132px;height:36px" role="img" aria-label="Photo of a residential development"></div><div class="blk" style="left:0;top:36px;width:132px;height:37px"></div><span class="word" style="left:6px;top:6px;font-size:6px;color:#fff">KESTREL</span><span class="hero" style="left:6px;top:50px;font-size:5px">Property</span><span class="p" style="left:50px;top:42px;width:76px;color:#fff">Add your text here</span></div>
  <div class="sl" style="left:382px;top:940px"><span class="t">Accreditation &amp; awards</span><span class="m">KESTREL</span><svg class="chart" style="left:6px;top:16px" width="122" height="50"><rect x="0" y="0" width="122" height="46" fill="none" stroke="#d9dbde" stroke-width=".6"/><g fill="#c4c6c9"><rect x="6" y="10" width="14" height="14"/><circle cx="38" cy="17" r="7"/><rect x="52" y="10" width="14" height="14"/><circle cx="84" cy="17" r="7"/><rect x="98" y="10" width="14" height="14"/></g><g fill="#a33" opacity=".6"><circle cx="14" cy="36" r="4"/><circle cx="38" cy="36" r="4"/><circle cx="60" cy="36" r="4"/><circle cx="84" cy="36" r="4"/><circle cx="106" cy="36" r="4"/></g></svg></div>

  <div class="sl" style="left:73px;top:1025px"><span class="t">Our portfolio (featured projects)</span><span class="m">KESTREL</span><div class="ph sky" style="left:6px;top:16px;width:28px;height:22px" role="img" aria-label="Project photo"></div><div class="ph" style="left:37px;top:16px;width:28px;height:22px" role="img" aria-label="Project photo"></div><div class="ph sky" style="left:68px;top:16px;width:28px;height:22px" role="img" aria-label="Project photo"></div><div class="ph" style="left:99px;top:16px;width:28px;height:22px" role="img" aria-label="Project photo"></div><div class="ph" style="left:6px;top:44px;width:28px;height:20px" role="img" aria-label="Project photo"></div><div class="ph sky" style="left:37px;top:44px;width:28px;height:20px" role="img" aria-label="Project photo"></div><div class="ph" style="left:68px;top:44px;width:28px;height:20px" role="img" aria-label="Project photo"></div><div class="ph sky" style="left:99px;top:44px;width:28px;height:20px" role="img" aria-label="Project photo"></div></div>
  <div class="sl maroon" style="left:228px;top:1025px"><span class="word" style="left:8px;top:10px;font-size:7px;color:#fff">KESTREL</span><span class="hero" style="left:76px;top:50px;font-size:5px">Template</span><span class="p" style="left:86px;top:57px">Slide ideas</span></div>
  <div class="sl" style="left:382px;top:1025px"><span class="t">Your slide title here</span><span class="m">KESTREL</span><span class="p" style="left:5px;top:11px;width:122px">Add a short paragraph of text here</span><svg class="chart" style="left:6px;top:22px" width="10" height="48"><g fill="#8f2b22"><circle cx="4" cy="4" r="3.5"/><circle cx="4" cy="20" r="3.5"/><circle cx="4" cy="36" r="3.5"/></g></svg><span class="p" style="left:18px;top:22px;width:100px">Add your text here<br><br><br><br>Add your text here<br><br><br><br>Add your text here</span></div>

  <div class="sl" style="left:73px;top:1112px"><span class="t">Your slide title here</span><span class="m">KESTREL</span><div class="ph sky" style="left:5px;top:14px;width:38px;height:52px" role="img" aria-label="Photo of trees and houses"></div><span class="p" style="left:48px;top:14px;width:80px">Add your text here<br><br>Add your text here<br><br>Add your text here</span></div>
  <div class="sl" style="left:228px;top:1112px"><span class="t">Your slide title here (about us)</span><span class="m">KESTREL</span><div class="ph" style="left:5px;top:14px;width:58px;height:30px" role="img" aria-label="Photo of a gated entrance"></div><span class="p" style="left:68px;top:14px;width:60px">Add your text here</span><span class="p" style="left:8px;top:52px">Title one &nbsp; Title two &nbsp; Title three</span></div>
  <div class="sl" style="left:382px;top:1112px"><span class="t">Your slide title here (about us)</span><span class="m">KESTREL</span><div class="ph sky" style="left:5px;top:14px;width:40px;height:52px" role="img" aria-label="Photo of a housing street"></div><div class="blk" style="left:48px;top:14px;width:38px;height:52px;background:var(--charcoal)"></div><span class="p" style="left:92px;top:16px;width:36px">Add your text here</span></div>

  <!-- right column set -->
  <div class="sl" style="left:680px;top:107px"><span class="t">Your slide title here (our employees)</span><span class="m">KESTREL</span><div class="ph sky" style="left:10px;top:20px;width:22px;height:26px" role="img" aria-label="Staff portrait placeholder"></div><div class="ph sky" style="left:40px;top:20px;width:22px;height:26px" role="img" aria-label="Staff portrait placeholder"></div><div class="ph sky" style="left:70px;top:20px;width:22px;height:26px" role="img" aria-label="Staff portrait placeholder"></div><div class="ph sky" style="left:100px;top:20px;width:22px;height:26px" role="img" aria-label="Staff portrait placeholder"></div><span class="p" style="left:10px;top:52px">Name &nbsp;&nbsp;&nbsp;&nbsp; Name &nbsp;&nbsp;&nbsp;&nbsp; Name &nbsp;&nbsp;&nbsp;&nbsp; Name</span></div>
  <div class="sl" style="left:834px;top:107px"><div class="blk" style="left:0;top:0;width:50px;height:73px;background:var(--charcoal)"></div><span class="t" style="color:#fff">Your slide title</span><span class="m">KESTREL</span><span class="p" style="left:5px;top:14px;width:40px;color:#ddd">Add your text here</span><svg class="chart" style="left:56px;top:28px" width="74" height="40"><g fill="#8f2b22"><circle cx="4" cy="4" r="3"/><circle cx="4" cy="16" r="3"/><circle cx="4" cy="28" r="3"/><circle cx="42" cy="4" r="3"/><circle cx="42" cy="16" r="3"/><circle cx="42" cy="28" r="3"/></g></svg></div>
  <div class="sl" style="left:988px;top:107px"><span class="t">Your slide title here</span><span class="m">KESTREL</span><svg class="chart" style="left:4px;top:14px" width="124" height="56"><g fill="#3a3d42"><rect x="0" y="0" width="28" height="6"/><rect x="31" y="0" width="28" height="6" fill="#9a9ea4"/><rect x="62" y="0" width="28" height="6" fill="#5e8a7d"/><rect x="93" y="0" width="28" height="6"/></g><g fill="#eceef0"><rect x="0" y="9" width="121" height="5"/><rect x="0" y="18" width="121" height="5"/><rect x="0" y="27" width="121" height="5"/><rect x="0" y="36" width="121" height="5"/></g><g fill="#3a3d42"><rect x="0" y="46" width="28" height="6"/><rect x="31" y="46" width="28" height="6" fill="#9a9ea4"/><rect x="62" y="46" width="28" height="6" fill="#5e8a7d"/><rect x="93" y="46" width="28" height="6"/></g></svg></div>

  <div class="sl" style="left:680px;top:192px"><span class="t">Your slide title here</span><span class="m">KESTREL</span><svg class="chart" style="left:6px;top:20px" width="44" height="44"><circle cx="22" cy="22" r="17" fill="none" stroke="#3a3d42" stroke-width="6"/><circle cx="22" cy="22" r="17" fill="none" stroke="#8f2b22" stroke-width="6" stroke-dasharray="70 107" transform="rotate(-90 22 22)"/></svg><span class="p" style="left:56px;top:20px;width:70px">Add your text here<br><br>Add your text here<br><br>Add your text here</span></div>
  <div class="sl" style="left:834px;top:192px"><span class="t">Your slide title here</span><span class="m">KESTREL</span><svg class="chart" style="left:6px;top:16px" width="10" height="52"><g fill="#8f2b22"><circle cx="4" cy="4" r="3.5"/><circle cx="4" cy="17" r="3.5"/><circle cx="4" cy="30" r="3.5"/><circle cx="4" cy="43" r="3.5"/></g></svg><svg class="chart" style="left:68px;top:20px" width="60" height="44"><g fill="#c8cacd"><rect x="0" y="30" width="7" height="14"/><rect x="10" y="24" width="7" height="20"/><rect x="20" y="18" width="7" height="26" fill="#8a8e94"/><rect x="30" y="12" width="7" height="32"/><rect x="40" y="6" width="7" height="38" fill="#8a8e94"/></g></svg></div>
  <div class="sl" style="left:988px;top:192px"><span class="t">Your slide title here</span><span class="m">KESTREL</span><span class="p" style="left:5px;top:11px;width:122px">Add a short paragraph of text here</span><div class="blk" style="left:6px;top:30px;width:58px;height:36px"></div><div class="blk" style="left:67px;top:30px;width:58px;height:36px;background:var(--charcoal)"></div><span class="p" style="left:10px;top:34px;color:#fff">Pros</span><span class="p" style="left:71px;top:34px;color:#fff">Cons</span></div>

  <div class="sl" style="left:680px;top:279px"><span class="t">Your slide title here</span><span class="m">KESTREL</span><svg class="chart" style="left:16px;top:26px" width="100" height="12"><g fill="none" stroke="#8f2b22" stroke-width=".8"><rect x="2" y="2" width="7" height="7"/><rect x="34" y="2" width="7" height="7"/><rect x="66" y="2" width="7" height="7"/><rect x="90" y="2" width="7" height="7"/></g></svg><span class="p" style="left:6px;top:50px;width:120px">Add a short paragraph of text here</span></div>
  <div class="sl" style="left:834px;top:279px"><span class="t">Your slide title here</span><span class="m">KESTREL</span><div class="blk" style="left:0;top:22px;width:132px;height:34px"></div><svg class="chart" style="left:10px;top:26px" width="114" height="16"><g fill="none" stroke="#fff" stroke-width="1"><circle cx="8" cy="8" r="6"/><circle cx="34" cy="8" r="6"/><circle cx="60" cy="8" r="6"/><circle cx="86" cy="8" r="6"/><circle cx="108" cy="8" r="5"/></g></svg></div>
  <div class="sl dark" style="left:988px;top:279px"><div class="ph dim" style="left:0;top:0;width:132px;height:70px" role="img" aria-label="Photo of an apartment block at dusk"></div><span class="t">Your slide title here</span><div class="blk" style="left:6px;top:24px;width:40px;height:40px;background:rgba(143,43,34,.85)"></div><span class="p" style="left:9px;top:28px;width:34px;color:#fff">Add your text here</span></div>

  <div class="sl" style="left:680px;top:370px"><div class="blk" style="left:0;top:0;width:48px;height:73px"></div><span class="t">Your slide title</span><span class="p" style="left:5px;top:12px;width:40px;color:#fff">Add your text here in a short line</span><div class="ph dim" style="left:48px;top:0;width:84px;height:40px" role="img" aria-label="Photo of a building"></div><svg class="chart" style="left:54px;top:46px" width="76" height="20"><g fill="#fff" stroke="#8f2b22" stroke-width="2"><circle cx="10" cy="10" r="8"/><circle cx="38" cy="10" r="8"/><circle cx="66" cy="10" r="8"/></g><g font-family="Montserrat,sans-serif" font-size="5" font-weight="800" fill="#8f2b22" text-anchor="middle"><text x="10" y="12">5%</text><text x="38" y="12">3%</text><text x="66" y="12">2%</text></g></svg></div>
  <div class="sl" style="left:834px;top:370px"><span class="t">Your slide title here</span><span class="m">KESTREL</span><svg class="chart" style="left:6px;top:22px" width="120" height="40"><line x1="0" y1="20" x2="120" y2="20" stroke="#c8cacd" stroke-width="1"/><g fill="#3a3d42"><path d="M8 4h10v8l-5 4-5-4z"/><path d="M32 4h10v8l-5 4-5-4z"/><path d="M56 4h10v8l-5 4-5-4z"/><path d="M80 4h10v8l-5 4-5-4z"/><path d="M104 4h10v8l-5 4-5-4z"/></g><g fill="#8f2b22"><circle cx="13" cy="20" r="2"/><circle cx="37" cy="20" r="2"/><circle cx="61" cy="20" r="2"/><circle cx="85" cy="20" r="2"/><circle cx="109" cy="20" r="2"/></g></svg></div>
  <div class="sl dark" style="left:988px;top:370px"><div class="ph dim" style="left:0;top:0;width:132px;height:70px" role="img" aria-label="Photo of a street at night"></div><span class="t">Your slide title here</span><svg class="chart" style="left:20px;top:26px" width="94" height="40"><g fill="#8f2b22"><rect x="0" y="0" width="30" height="4"/><rect x="32" y="0" width="30" height="4"/><rect x="64" y="0" width="30" height="4"/></g><g fill="rgba(255,255,255,.25)"><rect x="0" y="7" width="94" height="4"/><rect x="0" y="14" width="94" height="4"/><rect x="0" y="21" width="94" height="4"/><rect x="0" y="28" width="94" height="4"/></g></svg></div>

  <div class="sl" style="left:680px;top:455px"><span class="t">Your slide title here (table data)</span><span class="m">KESTREL</span><div class="ph dim" style="left:0;top:12px;width:52px;height:58px" role="img" aria-label="Photo of an office interior"></div><svg class="chart" style="left:58px;top:22px" width="70" height="44"><g fill="#8f2b22"><rect x="0" y="0" width="22" height="4"/><rect x="24" y="0" width="22" height="4"/><rect x="48" y="0" width="22" height="4"/></g><g fill="#eceef0"><rect x="0" y="7" width="70" height="4"/><rect x="0" y="14" width="70" height="4"/><rect x="0" y="21" width="70" height="4"/><rect x="0" y="28" width="70" height="4"/><rect x="0" y="35" width="70" height="4"/></g></svg></div>
  <div class="sl" style="left:834px;top:455px"><span class="t">Your slide title here</span><span class="m">KESTREL</span><svg class="chart" style="left:8px;top:22px" width="118" height="46"><g stroke="#e0e2e4" stroke-width=".6"><line x1="0" y1="8" x2="118" y2="8"/><line x1="0" y1="18" x2="118" y2="18"/><line x1="0" y1="28" x2="118" y2="28"/><line x1="0" y1="38" x2="118" y2="38"/></g><g fill="#8f2b22" font-family="Montserrat,sans-serif" font-size="6" text-anchor="middle"><text x="70" y="14">✓</text><text x="100" y="14">✕</text><text x="70" y="24">✕</text><text x="100" y="24">✓</text><text x="70" y="34">✓</text><text x="100" y="34">✓</text></g></svg></div>
  <div class="sl" style="left:988px;top:455px"><div class="ph" style="left:0;top:0;width:60px;height:70px" role="img" aria-label="Photo of a townhouse courtyard"></div><span class="t" style="left:64px">Your title here</span><span class="m">KESTREL</span><span class="p" style="left:64px;top:14px;width:64px">Add your text here</span><svg class="chart" style="left:64px;top:36px" width="10" height="30"><g fill="#8f2b22"><circle cx="4" cy="4" r="3"/><circle cx="4" cy="16" r="3"/></g></svg></div>

  <div class="sl" style="left:680px;top:542px"><span class="t">Your slide title here</span><span class="m">KESTREL</span><span class="p" style="left:5px;top:11px;width:122px">Add a short paragraph of text here</span><svg class="chart" style="left:4px;top:36px" width="124" height="14"><g fill="#8f2b22"><path d="M0 0h22l4 7-4 7H0l4-7z"/><path d="M25 0h22l4 7-4 7H25l4-7z" fill="#6f1f18"/><path d="M50 0h22l4 7-4 7H50l4-7z"/><path d="M75 0h22l4 7-4 7H75l4-7z" fill="#6f1f18"/><path d="M100 0h20l4 7-4 7h-20l4-7z"/></g></svg></div>
  <div class="sl" style="left:834px;top:542px"><span class="t">Your slide title here</span><span class="m">KESTREL</span><svg class="chart" style="left:8px;top:20px" width="118" height="44"><g fill="#3a3d42"><rect x="0" y="0" width="26" height="5"/><rect x="30" y="0" width="26" height="5"/><rect x="60" y="0" width="26" height="5"/><rect x="90" y="0" width="26" height="5"/></g><g fill="#eceef0"><rect x="0" y="8" width="26" height="32"/><rect x="30" y="8" width="26" height="32"/><rect x="60" y="8" width="26" height="32"/><rect x="90" y="8" width="26" height="32"/></g></svg></div>
  <div class="sl" style="left:988px;top:542px"><span class="t">Your slide title here</span><span class="m">KESTREL</span><svg class="chart" style="left:46px;top:18px" width="40" height="40"><circle cx="20" cy="20" r="16" fill="none" stroke="#8f2b22" stroke-width="6" stroke-dasharray="14 3"/><circle cx="20" cy="20" r="8" fill="#3a3d42"/></svg><span class="p" style="left:6px;top:24px;width:38px">Add your text here</span><span class="p" style="left:90px;top:24px;width:38px">Add your text here</span></div>

  <div class="sl" style="left:680px;top:630px"><span class="t">Your slide title here</span><span class="m">KESTREL</span><span class="p" style="left:5px;top:14px;width:48px">Add a short paragraph of text here</span><svg class="chart" style="left:70px;top:14px" width="56" height="46"><g fill="none" stroke="#8f2b22" stroke-width=".8"><circle cx="10" cy="8" r="4"/><circle cx="44" cy="8" r="4"/><circle cx="10" cy="34" r="4"/><circle cx="44" cy="34" r="4"/></g></svg></div>
  <div class="sl" style="left:834px;top:630px"><span class="t">Your slide title here</span><span class="m">KESTREL</span><svg class="chart" style="left:48px;top:20px" width="40" height="40"><circle cx="20" cy="20" r="15" fill="none" stroke="#8f2b22" stroke-width="7" stroke-dasharray="18 5"/><circle cx="20" cy="20" r="8" fill="#3a3d42"/></svg><span class="p" style="left:6px;top:22px;width:40px">Add your text here</span><span class="p" style="left:92px;top:22px;width:36px">Add your text here</span></div>
  <div class="sl dark" style="left:988px;top:630px"><div class="ph dim" style="left:0;top:0;width:132px;height:70px" role="img" aria-label="Photo of a building facade"></div><div style="position:absolute;left:18px;top:30px;width:94px;height:26px;background:#fff"></div><span class="p" style="left:22px;top:33px;width:86px;color:#555">“ Add a short quote here to share a key message. ”</span></div>

  <div class="sl" style="left:680px;top:716px"><div class="ph dim" style="left:0;top:0;width:132px;height:30px" role="img" aria-label="Photo of a site at dusk"></div><span class="t" style="color:#fff">Enter your slide title</span><div style="position:absolute;left:6px;top:22px;width:18px;height:40px;background:#fff;border:.5px solid #ddd"></div><div style="position:absolute;left:28px;top:22px;width:18px;height:40px;background:#fff;border:.5px solid #ddd"></div><span class="p" style="left:52px;top:36px;width:74px">Add your text here</span></div>
  <div class="sl" style="left:834px;top:716px"><span class="t">Your slide title here</span><span class="m">KESTREL</span><svg class="chart" style="left:6px;top:18px" width="10" height="46"><g fill="#8f2b22"><circle cx="4" cy="4" r="3"/><circle cx="4" cy="18" r="3"/><circle cx="4" cy="32" r="3"/></g></svg><div class="ph" style="left:70px;top:22px;width:56px;height:36px" role="img" aria-label="Photo of a residential complex"></div><span class="p" style="left:16px;top:18px;width:50px">Add your text here</span></div>
  <div class="sl" style="left:988px;top:716px"><span class="t">Your slide title here</span><span class="m">KESTREL</span><svg class="chart" style="left:8px;top:16px" width="46" height="46"><circle cx="23" cy="23" r="18" fill="none" stroke="#d6d8db" stroke-width="8"/><circle cx="23" cy="23" r="18" fill="none" stroke="#8f2b22" stroke-width="8" stroke-dasharray="56 113" transform="rotate(-90 23 23)"/></svg><span class="p" style="left:66px;top:18px;width:60px">Add your text here<br><br>Add your text here<br><br>Add your text here</span></div>

  <div class="sl" style="left:680px;top:802px"><span class="t">Your slide title here</span><span class="m">KESTREL</span><svg class="chart" style="left:6px;top:22px" width="56" height="42"><g><rect x="2" y="14" width="5" height="26" fill="#8f2b22"/><rect x="8" y="22" width="5" height="18" fill="#3a3d42"/><rect x="16" y="6" width="5" height="34" fill="#8f2b22"/><rect x="22" y="18" width="5" height="22" fill="#5e8a7d"/><rect x="30" y="12" width="5" height="28" fill="#8f2b22"/><rect x="36" y="4" width="5" height="36" fill="#5e8a7d"/><rect x="44" y="20" width="5" height="20" fill="#8f2b22"/></g></svg><span class="p" style="left:70px;top:22px;width:56px">Title goes here<br><br>Add your text here<br><br>Add your text here</span></div>
  <div class="sl" style="left:834px;top:802px"><span class="t">Your slide title here</span><span class="m">KESTREL</span><svg class="chart" style="left:80px;top:22px" width="44" height="36"><ellipse cx="22" cy="20" rx="20" ry="12" fill="#c8cacd"/><path d="M22 20 L22 8 A20 12 0 0 1 40 26 Z" fill="#8f2b22"/></svg><span class="p" style="left:6px;top:22px;width:70px">Add your text here<br><br>Add your text here</span></div>
  <div class="sl" style="left:988px;top:802px"><span class="t">Your slide title here</span><span class="m">KESTREL</span><svg class="chart" style="left:6px;top:22px" width="50" height="36"><polyline points="0,30 12,14 24,24 36,8 48,20" fill="none" stroke="#8f2b22" stroke-width="1"/><polyline points="0,10 12,26 24,14 36,28 48,12" fill="none" stroke="#9a9ea4" stroke-width="1"/></svg><svg class="chart" style="left:64px;top:22px" width="62" height="36"><g fill="#8f2b22"><rect x="0" y="0" width="50" height="3"/><rect x="0" y="10" width="40" height="3"/><rect x="0" y="20" width="56" height="3"/><rect x="0" y="30" width="30" height="3"/></g><g fill="#3a3d42"><rect x="0" y="4" width="36" height="3"/><rect x="0" y="14" width="48" height="3"/><rect x="0" y="24" width="28" height="3"/></g></svg></div>

  <div class="sl" style="left:680px;top:893px"><span class="t">Your slide title here</span><span class="m">KESTREL</span><svg class="chart" style="left:6px;top:24px" width="76" height="40"><polyline points="0,26 8,18 16,28 24,12 32,22 40,6 48,24 56,14 64,30 72,20" fill="none" stroke="#8f2b22" stroke-width="1"/><line x1="0" y1="36" x2="76" y2="36" stroke="#c8cacd" stroke-width=".6"/></svg><span class="p" style="left:84px;top:22px;width:44px">Add your text here<br><br>Add your text here</span></div>
  <div class="sl" style="left:834px;top:893px"><span class="t">Your slide title here</span><span class="m">KESTREL</span><svg class="chart" style="left:50px;top:22px" width="36" height="36"><circle cx="18" cy="18" r="15" fill="none" stroke="#8f2b22" stroke-width="3"/></svg><span class="word" style="left:56px;top:37px;font-size:4px">KESTREL</span><span class="p" style="left:6px;top:22px;width:40px">Add your text here<br><br>Add your text here</span><span class="p" style="left:92px;top:22px;width:36px">Add your text here<br><br>Add your text here</span></div>
  <div class="sl" style="left:988px;top:893px"><span class="t">Your slide title here</span><span class="m">KESTREL</span><svg class="chart" style="left:4px;top:14px" width="126" height="56"><polygon points="0,56 0,0 40,56" fill="#8f2b22"/><polygon points="126,4 126,56 86,56" fill="#8f2b22"/><g fill="#3a3d42"><rect x="28" y="8" width="10" height="7"/><rect x="28" y="22" width="10" height="7"/><rect x="28" y="36" width="10" height="7"/></g></svg><span class="p" style="left:46px;top:22px;width:44px">Add your text here<br><br>Add your text here</span></div>

  <div class="sl" style="left:680px;top:978px"><span class="t">Your slide title here</span><span class="m">KESTREL</span><svg class="chart" style="left:42px;top:16px" width="48" height="50"><g><polygon points="10,2 18,6 18,14 10,18 2,14 2,6" fill="#8f2b22"/><polygon points="28,2 36,6 36,14 28,18 20,14 20,6" fill="#3a3d42"/><polygon points="38,18 46,22 46,30 38,34 30,30 30,22" fill="#8f2b22"/><polygon points="19,18 27,22 27,30 19,34 11,30 11,22" fill="#3a3d42"/><polygon points="10,34 18,38 18,46 10,50 2,46 2,38" fill="#3a3d42"/><polygon points="28,34 36,38 36,46 28,50 20,46 20,38" fill="#8f2b22"/></g></svg><span class="p" style="left:6px;top:22px;width:34px">Add your text here</span><span class="p" style="left:94px;top:22px;width:34px">Add your text here</span></div>
  <div class="sl" style="left:834px;top:978px"><span class="t">Your slide title here</span><span class="m">KESTREL</span><svg class="chart" style="left:10px;top:26px" width="114" height="28"><path d="M2 14 a12 12 0 0 1 24 0 a12 12 0 0 0 24 0 a12 12 0 0 1 24 0 a12 12 0 0 0 24 0" fill="none" stroke="#3a3d42" stroke-width="4"/><g fill="#8f2b22"><circle cx="14" cy="14" r="4"/><circle cx="38" cy="14" r="4"/><circle cx="62" cy="14" r="4"/><circle cx="86" cy="14" r="4"/></g></svg></div>
  <div class="sl" style="left:988px;top:978px"><span class="t">Your slide title here</span><span class="m">KESTREL</span><svg class="chart" style="left:8px;top:22px" width="96" height="40"><g><polygon points="0,38 8,6 16,38" fill="#8f2b22"/><polygon points="18,38 26,14 34,38" fill="#3a3d42"/><polygon points="36,38 44,2 52,38" fill="#5e8a7d"/><polygon points="54,38 62,18 70,38" fill="#8f2b22"/><polygon points="72,38 80,10 88,38" fill="#3a3d42"/></g></svg></div>

  <div class="sl" style="left:680px;top:1064px"><span class="t">Your slide title here</span><span class="m">KESTREL</span><div style="position:absolute;left:8px;top:20px;width:40px;height:30px;background:#2b2e33;border-radius:2px"></div><div class="ph dim" style="left:10px;top:22px;width:36px;height:26px" role="img" aria-label="Photo of an apartment building on a laptop screen"></div><div style="position:absolute;left:4px;top:50px;width:48px;height:2px;background:#9a9ea4"></div><span class="p" style="left:58px;top:20px;width:70px">Add your text here<br><br>Add your text here</span></div>
  <div class="sl dark" style="left:834px;top:1064px"><div class="ph dim" style="left:0;top:0;width:132px;height:40px" role="img" aria-label="Aerial photo of a housing estate"></div><span class="hero" style="left:88px;top:12px;font-size:4.5px">Thank you</span><div style="position:absolute;left:0;top:40px;width:132px;height:33px;background:#fff"></div><span class="word" style="left:6px;top:50px;font-size:6px">KESTREL</span><span class="p" style="left:50px;top:46px;width:78px;color:#666">Head office<br>12 Example Road<br>+00 000 000 000</span></div>
</div>
</body>
</html>
```